Speisekarten-Design für persisches Restaurant
Zielgruppe
persisches Restaurant, möchte eine Karte mit schlichtem Design
Aufgabenstellung
bislang hatten wir ein Din A4 Karte mit vier Seiten. Kann gerne übernommen werden

```html
<!DOCTYPE html>
<html lang="de">
<head>
<meta charset="utf-8">
<title>Getränkekarte</title>
<link href="https://fonts.googleapis.com/css2?family=Barlow+Condensed:wght@400;500;600&display=swap" rel="stylesheet">
<style>
:root{
  --bg:#ffffff;
  --paper:#fdfdfc;
  --frame:#cdb89a;
  --band-dark:#3a3838;
  --band-soft:#6a6765;
  --gold:#a6865a;
  --ink:#2f2d2b;
  --rule:#c9b79c;
}
*{box-sizing:border-box;margin:0;padding:0}
html,body{width:1200px;height:848px;overflow:hidden;background:var(--bg)}
body{position:relative;font-family:"Barlow Condensed",sans-serif;text-transform:uppercase}
.page{position:absolute;top:76px;width:498px;height:704px;background:var(--paper);box-shadow:0 1px 5px rgba(0,0,0,.22)}
.page--drinks{left:78px}
.page--allergens{left:627px}
.page__frame{position:absolute;inset:11px;border:2px solid var(--frame)}
.border-band{position:absolute;left:18px;width:462px;height:20px}
.border-band--top{top:19px;background:linear-gradient(to bottom,var(--band-dark),var(--band-soft))}
.border-band--bottom{bottom:19px;background:linear-gradient(to top,var(--band-dark),var(--band-soft))}
.section-title{position:absolute;left:53px;width:392px;display:flex;align-items:center;gap:6px;font-size:16.5px;font-weight:400;color:var(--ink);white-space:nowrap}
.section-title::before,.section-title::after{content:"";flex:1;height:1.5px;background:var(--rule)}
.menu{position:absolute;left:53px;width:392px;list-style:none}
.menu__item{display:flex;align-items:baseline;height:19px;font-size:10.5px;font-weight:500;color:var(--gold)}
.menu__dots{flex:1;border-bottom:1.5px dotted var(--gold);margin:0 3px;transform:translateY(-3px)}
.menu__size{width:30px;text-align:right}
.menu__price{width:30px;text-align:right}
.menu__inline{margin-left:10px}
sup{font-size:5px;vertical-align:6px;margin-left:1px}
.brewery{position:absolute;left:53px;top:240px;font-size:10.5px;font-style:italic;font-weight:600;color:var(--gold)}
.legend-title{position:absolute;left:51px;width:400px;display:flex;align-items:center;gap:5px;font-size:15px;font-weight:400;color:var(--ink);white-space:nowrap}
.legend-title::before,.legend-title::after{content:"";width:7px;height:1.5px;background:var(--gold)}
.legend-heading{position:absolute;left:51px;font-size:16.5px;font-weight:400;color:var(--ink)}
.legend{position:absolute;left:51px;list-style:none}
.legend__item{display:flex;align-items:baseline;height:15.8px;font-size:9.5px;font-weight:600;color:var(--ink)}
.legend__key{width:9px}
.legend__dots{width:47px;border-bottom:1.5px dotted var(--ink);margin:0 3px 0 2px;transform:translateY(-3px)}
.brand{position:absolute;left:356px;top:132px;display:flex;align-items:center;gap:6px;font-size:24px;font-weight:600;color:var(--ink)}
.brand__dot{width:20px;height:20px;border-radius:50%;background:#e5b82a}
</style>
</head>
<body>

<section class="page page--drinks">
  <div class="page__frame"></div>
  <div class="border-band border-band--top" role="img" aria-label="Zickzack-Bordüre"></div>

  <h2 class="section-title" style="top:62px">Alkoholfreie Getränke // Softdrinks</h2>
  <ul class="menu" style="top:86px">
    <li class="menu__item"><span>Wasser</span><span class="menu__dots"></span><span>0,2 L</span><span class="menu__inline">2,50</span><span class="menu__dots" style="flex:0 0 40px"></span><span class="menu__size">0,75 L</span><span class="menu__price">6,50</span></li>
    <li class="menu__item"><span>Rota Cola<sup>4 7</sup> / Rota Light<sup>4 6 7 10</sup> / Rota Zero<sup>4 6 7 10</sup></span><span class="menu__dots"></span><span class="menu__size">0,33 L</span><span class="menu__price">2,90</span></li>
    <li class="menu__item"><span>Klarlimo / Orangello<sup>3 4</sup> / Duo Mix<sup>3 4 7</sup></span><span class="menu__dots"></span><span class="menu__size">0,33 L</span><span class="menu__price">2,90</span></li>
    <li class="menu__item"><span>Apfelschorle</span><span class="menu__dots"></span><span class="menu__size">0,33 L</span><span class="menu__price">2,90</span></li>
    <li class="menu__item"><span>Dough</span><span class="menu__dots"></span><span class="menu__size">0,25 L</span><span class="menu__price">2,90</span></li>
    <li class="menu__item"><span>Hausgemachte Limonade</span><span class="menu__dots"></span><span class="menu__size">0,5 L</span><span class="menu__price">4,50</span></li>
  </ul>

  <h2 class="section-title" style="top:220px">Bier // Beer</h2>
  <p class="brewery">Aurel</p>
  <ul class="menu" style="top:256px">
    <li class="menu__item"><span>Pils / Alkoholfrei</span><span class="menu__dots"></span><span class="menu__size">0,33 L</span><span class="menu__price">2,50</span></li>
    <li class="menu__item"><span>Radler / Radler alkoholfrei</span><span class="menu__dots"></span><span class="menu__size">0,33 L</span><span class="menu__price">3,00</span></li>
    <li class="menu__item"><span>Weizen hell/dunkel/alkoholfrei</span><span class="menu__dots"></span><span class="menu__size">0,5 L</span><span class="menu__price">4,50</span></li>
  </ul>

  <h2 class="section-title" style="top:329px">Warme Getränke // Warm Drniks</h2>
  <ul class="menu" style="top:355px">
    <li class="menu__item"><span>Schwarzer Tee</span><span class="menu__dots"></span><span class="menu__price">1,00</span></li>
    <li class="menu__item"><span>Frischer Minztee</span><span class="menu__dots"></span><span class="menu__price">2,00</span></li>
    <li class="menu__item"><span>Espresso</span><span class="menu__dots"></span><span class="menu__price">1,50</span></li>
    <li class="menu__item"><span>Doppelter Espresso</span><span class="menu__dots"></span><span class="menu__price">2,50</span></li>
    <li class="menu__item"><span>Kaffee</span><span class="menu__dots"></span><span class="menu__price">2,50</span></li>
    <li class="menu__item"><span>Cappuccino</span><span class="menu__dots"></span><span class="menu__price">2,80</span></li>
    <li class="menu__item"><span>Milchkaffee</span><span class="menu__dots"></span><span class="menu__price">2,80</span></li>
  </ul>

  <div class="border-band border-band--bottom" role="img" aria-label="Zickzack-Bordüre"></div>
</section>

<section class="page page--allergens">
  <div class="page__frame"></div>
  <div class="border-band border-band--top" role="img" aria-label="Zickzack-Bordüre"></div>

  <h2 class="legend-title" style="top:80px">Liste der deklarationspflichtigen Allergene und Zusatzstoffe</h2>

  <div class="brand"><span class="brand__dot"></span><span>KHR</span></div>

  <h3 class="legend-heading" style="top:126px">Deklarationspflichtige Zusatzstoffe</h3>
  <ul class="legend" style="top:151px">
    <li class="legend__item"><span class="legend__key">1</span><span class="legend__dots"></span><span>Mit Farbstoffen</span></li>
    <li class="legend__item"><span class="legend__key">2</span><span class="legend__dots"></span><span>Mit Konservierungsstoff</span></li>
    <li class="legend__item"><span class="legend__key">3</span><span class="legend__dots"></span><span>Mit Antioxidationsmittel</span></li>
    <li class="legend__item"><span class="legend__key">4</span><span class="legend__dots"></span><span>Mit Geschmacksverstärker</span></li>
    <li class="legend__item"><span class="legend__key">5</span><span class="legend__dots"></span><span>Geschwefelt</span></li>
    <li class="legend__item"><span class="legend__key">6</span><span class="legend__dots"></span><span>Geschwärzt</span></li>
    <li class="legend__item"><span class="legend__key">7</span><span class="legend__dots"></span><span>Mit Phosphat</span></li>
    <li class="legend__item"><span class="legend__key">8</span><span class="legend__dots"></span><span>Mit Milcheiweiss (bei Fleischerzeugnissen)</span></li>
    <li class="legend__item"><span class="legend__key">9</span><span class="legend__dots"></span><span>Koffeinhaltig</span></li>
    <li class="legend__item"><span class="legend__key">10</span><span class="legend__dots"></span><span>Chininhaltig</span></li>
    <li class="legend__item"><span class="legend__key">11</span><span class="legend__dots"></span><span>Mit Süssungsmittel</span></li>
    <li class="legend__item"><span class="legend__key">12</span><span class="legend__dots"></span><span>Gewachst</span></li>
  </ul>

  <h3 class="legend-heading" style="top:364px">Deklarationspflichtige Allergene</h3>
  <ul class="legend" style="top:389px">
    <li class="legend__item"><span class="legend__key">A</span><span class="legend__dots"></span><span>Glutenhaltiges Getreide</span></li>
    <li class="legend__item"><span class="legend__key">B</span><span class="legend__dots"></span><span>Krebstiere und daraus gewonnene Erzeugnisse</span></li>
    <li class="legend__item"><span class="legend__key">C</span><span class="legend__dots"></span><span>Eier und daraus gewonnene Erzeugnisse</span></li>
    <li class="legend__item"><span class="legend__key">D</span><span class="legend__dots"></span><span>Fische und daraus gewonnene Erzeugnisse</span></li>
    <li class="legend__item"><span class="legend__key">E</span><span class="legend__dots"></span><span>Erdnüsse und daraus gewonnene Erzeugnisse</span></li>
    <li class="legend__item"><span class="legend__key">F</span><span class="legend__dots"></span><span>Soja(bohnen) und daraus gewonnene Erzeugnisse</span></li>
    <li class="legend__item"><span class="legend__key">G</span><span class="legend__dots"></span><span>Milch und daraus gewonnene Erzeugnisse</span></li>
    <li class="legend__item"><span class="legend__key">H</span><span class="legend__dots"></span><span>Schalenfrüchte</span></li>
    <li class="legend__item"><span class="legend__key">I</span><span class="legend__dots"></span><span>Sellerie und daraus gewonnene Erzeugnisse</span></li>
    <li class="legend__item"><span class="legend__key">J</span><span class="legend__dots"></span><span>Senf und daraus gewonnene Erzeugnisse</span></li>
    <li class="legend__item"><span class="legend__key">K</span><span class="legend__dots"></span><span>Sesamsamen und daraus gewonnene Erzeugnisse</span></li>
    <li class="legend__item"><span class="legend__key">L</span><span class="legend__dots"></span><span>Schwefeldioxid und Sulphite</span></li>
    <li class="legend__item"><span class="legend__key">M</span><span class="legend__dots"></span><span>Lupinen und daraus gewonnene Erzeugnisse</span></li>
    <li class="legend__item"><span class="legend__key">N</span><span class="legend__dots"></span><span>Weichtiere und daraus gewonnene Erzeugnisse</span></li>
  </ul>

  <div class="border-band border-band--bottom" role="img" aria-label="Zickzack-Bordüre"></div>
</section>
</body>
</html>
```